Pagelink Cover Photo & Mailchimp Template for Greyhound Racing Club

Create a consistent, professional visual identity across Pagelink and email communications that promotes WTLB as a modern, community-focused greyhound racing club while respecting the heritage of greyhound racing.
Include WTLB logo.
Existing site https://www.pagelinkhub.net/MerrowfieldSprinters/

```html
<!DOCTYPE html>
<html lang="en">
<head>
<meta charset="utf-8">
<title>Merrowfield Greyhound Racing Club – Cover</title>
<link rel="stylesheet" href="https://fonts.googleapis.com/css2?family=Montserrat:wght@500;600;700;800&family=Open+Sans:wght@400;600&display=swap">
<style>
  :root {
    --navy: #1d3a66;
    --navy-deep: #17325c;
    --header-light: #e4e6e9;
    --header-mid: #b9c0c9;
    --band-light: #a8b0ba;
    --ink: #1a1c20;
    --brand-green: #2aa52e;
    --white: #ffffff;
    --sand: #c9b59c;
    --sand-light: #d9cab6;
    --field: #5d6b4f;
  }
  * { box-sizing: border-box; margin: 0; padding: 0; }
  html, body { width: 1200px; height: 908px; overflow: hidden; background: var(--white); }
  .cover {
    position: relative;
    width: 1200px;
    height: 908px;
    overflow: hidden;
    font-family: "Open Sans", Arial, sans-serif;
    color: var(--white);
  }
  .cover__header {
    position: absolute; left: 0; top: 0; width: 1200px; height: 162px;
    background: linear-gradient(90deg, var(--header-light) 0%, #d3d7dc 45%, var(--header-mid) 70%, var(--navy) 100%);
  }
  .brand {
    position: absolute; left: 68px; top: 40px;
    display: flex; align-items: center; gap: 30px;
    color: var(--ink);
    font-family: "Montserrat", Arial, sans-serif;
    font-weight: 700;
  }
  .brand__dot {
    width: 52px; height: 52px; border-radius: 50%;
    background: var(--brand-green);
    margin-left: 120px;
  }
  .brand__name { font-size: 40px; line-height: 1; letter-spacing: 0.5px; }
  .brand__tagline { font-size: 15px; letter-spacing: 5.5px; margin-top: 12px; margin-left: 14px; }

  .cover__photo {
    position: absolute; left: 0; top: 162px; width: 1200px; height: 608px;
    background:
      linear-gradient(180deg, #7c8c6a 0%, var(--field) 14%, #b9b4a6 26%, var(--sand-light) 40%, var(--sand) 70%, #bfa98e 100%);
  }
  .cover__shade {
    position: absolute; left: 0; top: 162px; width: 1200px; height: 608px;
    background: linear-gradient(90deg, rgba(29,58,102,0) 0%, rgba(29,58,102,0) 50%, rgba(29,58,102,0.55) 66%, rgba(29,58,102,0.9) 82%, var(--navy) 100%);
  }
  .cover__footer {
    position: absolute; left: 0; top: 770px; width: 1200px; height: 138px;
    background: linear-gradient(90deg, var(--band-light) 0%, #8e99a7 45%, #3f5880 75%, var(--navy-deep) 100%);
  }

  .hero {
    position: absolute; right: 57px; top: 420px;
    text-align: right;
  }
  .hero__title {
    font-family: "Montserrat", Arial, sans-serif;
    font-weight: 700;
    font-size: 72px;
    line-height: 1.06;
    letter-spacing: 0.5px;
  }
  .hero__subtitle {
    font-size: 25px; font-weight: 400; margin-top: 18px;
    text-align: center; margin-left: -10px;
  }
  .features {
    position: absolute; top: 645px; left: 700px; width: 440px;
    display: flex; justify-content: space-between;
    list-style: none;
  }
  .feature {
    display: flex; flex-direction: column; align-items: center; gap: 12px;
    font-size: 22px;
    width: 140px;
  }
  .feature__icon { width: 52px; height: 52px; }

  .follow {
    position: absolute; right: 52px; top: 843px;
    display: flex; align-items: center; gap: 14px;
    font-family: "Montserrat", Arial, sans-serif;
    font-weight: 600; font-size: 27px;
  }
  .follow__mark { width: 38px; height: 38px; border-radius: 5px; background: var(--white); }
</style>
</head>
<body>
<main class="cover">
  <header class="cover__header">
    <div class="brand">
      <span class="brand__dot"></span>
      <div>
        <div class="brand__name">Merrowfield</div>
        <div class="brand__tagline">GREYHOUND RACING CLUB</div>
      </div>
    </div>
  </header>

  <div class="cover__photo" role="img" aria-label="Photo of five greyhounds sprinting toward the camera on a sandy race track, dust kicking up, with a blurred fence and trees behind"></div>
  <div class="cover__shade"></div>
  <div class="cover__footer"></div>

  <section class="hero">
    <h1 class="hero__title">EXPERIENCE<br>THE THRILL</h1>
    <p class="hero__subtitle">Modern Racing, Community Heart</p>
  </section>

  <ul class="features">
    <li class="feature">
      <svg class="feature__icon" viewBox="0 0 52 52" aria-hidden="true">
        <circle cx="26" cy="26" r="24" fill="none" stroke="#fff" stroke-width="2.5"/>
        <rect x="14" y="16" width="24" height="21" rx="2" fill="none" stroke="#fff" stroke-width="2.2"/>
        <line x1="14" y1="22" x2="38" y2="22" stroke="#fff" stroke-width="2.2"/>
        <line x1="19" y1="12" x2="19" y2="18" stroke="#fff" stroke-width="2.2"/>
        <line x1="33" y1="12" x2="33" y2="18" stroke="#fff" stroke-width="2.2"/>
        <g fill="#fff">
          <rect x="17" y="25" width="3" height="3"/><rect x="22" y="25" width="3" height="3"/><rect x="27" y="25" width="3" height="3"/><rect x="32" y="25" width="3" height="3"/>
          <rect x="17" y="30" width="3" height="3"/><rect x="22" y="30" width="3" height="3"/><rect x="27" y="30" width="3" height="3"/><rect x="32" y="30" width="3" height="3"/>
        </g>
      </svg>
      Race Days
    </li>
    <li class="feature">
      <svg class="feature__icon" viewBox="0 0 52 52" aria-hidden="true">
        <circle cx="26" cy="26" r="24" fill="none" stroke="#fff" stroke-width="2.5"/>
        <path d="M18 14h16v7a8 8 0 0 1-16 0z" fill="#fff"/>
        <path d="M18 16h-4a5 5 0 0 0 5 7M34 16h4a5 5 0 0 1-5 7" fill="none" stroke="#fff" stroke-width="2"/>
        <rect x="24.5" y="28" width="3" height="6" fill="#fff"/>
        <rect x="19" y="34" width="14" height="4" rx="1" fill="#fff"/>
      </svg>
      Events
    </li>
    <li class="feature">
      <svg class="feature__icon" viewBox="0 0 52 52" aria-hidden="true">
        <circle cx="26" cy="26" r="24" fill="none" stroke="#fff" stroke-width="2.5"/>
        <g fill="#fff">
          <circle cx="26" cy="19" r="5"/>
          <path d="M17 36a9 9 0 0 1 18 0z"/>
          <circle cx="15" cy="22" r="3.5"/>
          <path d="M8 35a7 7 0 0 1 11-6 11 11 0 0 0-3 6z"/>
          <circle cx="37" cy="22" r="3.5"/>
          <path d="M44 35a7 7 0 0 0-11-6 11 11 0 0 1 3 6z"/>
        </g>
      </svg>
      Community
    </li>
  </ul>

  <a class="follow" href="https://www.pagelinkhub.net/MerrowfieldSprinters/" style="color:inherit;text-decoration:none;">
    <span class="follow__mark" aria-hidden="true"></span>
    Follow Us!
  </a>
</main>
</body>
</html>
```